Home Health Care Agency Needs a Website (Seeking a PSD)

We need a user friendly website for a Home Health Care Agency. Our service is for the elderly and disabled. Frequently the busy professional middle-aged married daughter will use the website to arrange in-home care for an aging parent. Therefore, our website is primarily geared towards middle-aged women. In-home care is typically 24 hours a day so, a feeling of trustworthiness and security should be effectively conveyed. (Seeking a PSD- however, if you also offer coding, please let us know the cost.)

Target Market(s)

Frequently the busy professional middle-aged married daughter (possibly out of state) will use the website to arrange in-home care for an aging parent.

Industry/Entity Type

Security

Requirements
Must have
• Website must be clean, uncluttered and professional. The following menu pages are requested: Home, About Us, Services, Resources, FAQ, Employment & Contact.
Should not have
• Must not be too whimsical.

```html
<!DOCTYPE html>
<html lang="en">
<head>
<meta charset="utf-8">
<title>Harbor Home Health</title>
<link href="https://fonts.googleapis.com/css2?family=Open+Sans:wght@400;600&family=Roboto:wght@300;400;500;700&display=swap" rel="stylesheet">
<style>
:root{
  --blue:#4cc8ef;
  --blue-dark:#17a9de;
  --topbar:#6b6b70;
  --footer:#6d6d72;
  --ink:#2f2f33;
  --text:#6a6a6a;
  --muted:#7d7d7d;
  --card-border:#d6d6d6;
  --dark-box:#1e1e20;
  --btn-grey:#6b6b70;
}
*{margin:0;padding:0;box-sizing:border-box}
html,body{width:1019px;height:1200px;overflow:hidden;background:#fff}
body{position:relative;font-family:"Roboto",sans-serif;color:var(--ink)}
.abs{position:absolute}

.topbar{left:0;top:0;width:1019px;height:26px;background:var(--topbar);color:#fff;font-size:11px}
.topbar .contact{position:absolute;top:6px;display:flex;align-items:center;gap:6px;white-space:nowrap}
.topbar svg{width:12px;height:12px}

.header{left:0;top:26px;width:1019px;height:78px;background:#fff}
.brand{position:absolute;left:136px;top:25px;display:flex;align-items:center;gap:7px}
.brand .dot{width:26px;height:26px;border-radius:50%;background:var(--blue)}
.brand .name{font-weight:500;font-size:18px;color:var(--blue);line-height:26px;white-space:nowrap}
.nav{position:absolute;right:137px;top:30px;display:flex;font-size:13.5px;color:#555}
.nav a{color:#555;text-decoration:none;padding:0 13px;border-left:1px solid #ccc;line-height:14px;white-space:nowrap}
.nav a:first-child{border-left:none;color:var(--blue)}
.nav a:last-child{padding-right:0}

.hero{left:0;top:104px;width:1019px;height:414px;background:radial-gradient(ellipse at 40% 45%,#b4b4b4 0%,#8a8a8a 45%,#4e4e4e 100%)}
.hero .arrow{position:absolute;top:159px;width:46px;height:98px}
.tagline{position:absolute;left:144px;top:188px;width:375px;height:37px;background:var(--blue);color:#fff;font-size:20px;font-weight:300;line-height:37px;padding-left:22px;white-space:nowrap}
.tagline b{font-weight:700}
.hours{position:absolute;left:144px;top:226px;width:70px;height:47px;background:var(--dark-box);color:#fff;font-size:25px;font-weight:300;line-height:47px;padding-left:14px}
.hours small{font-size:13px}
.hero .ring{position:absolute;left:586px;top:61px;width:288px;height:288px;border-radius:50%;background:#8d8d8d;padding:7px}
.hero .ring div{width:100%;height:100%;border-radius:50%;background:linear-gradient(135deg,#e9e4dc 0%,#c9d8e6 45%,#7fa3c8 75%,#c8a98a 100%)}

.section-title{font-size:14px;font-weight:300;color:var(--ink);letter-spacing:.2px;white-space:nowrap}
.section-title b{font-weight:500}

.card{top:601px;width:124px;height:207px;border:1px solid var(--card-border);background:#fff;text-align:center;font-family:"Open Sans",sans-serif}
.card .photo{height:85px}
.card .badge{position:absolute;left:48px;top:71px;width:26px;height:30px}
.card h3{margin-top:26px;font-size:10.5px;font-weight:400;color:#333;letter-spacing:.2px;white-space:nowrap}
.card p{margin:7px 12px 0;font-size:9.4px;line-height:12.5px;color:var(--muted)}
.card .more{position:absolute;left:0;right:0;top:177px;font-size:9px;color:var(--blue)}

.about-photo{left:137px;top:849px;width:263px;height:114px;background:linear-gradient(100deg,#5a1c22 0%,#b37f66 40%,#e2b59a 70%,#c58f76 100%)}
.about-text{font-size:9.8px;line-height:15.2px;letter-spacing:-.2px;color:var(--text);text-align:justify}
.btn{background:var(--btn-grey);color:#fff;font-size:10.5px;text-align:center;line-height:25px;border-radius:2px}

.faq{left:690px;top:559px;width:192px;height:496px;background:var(--blue);font-family:"Open Sans",sans-serif;color:#fff}
.faq .flag{position:absolute;left:14px;top:0;width:26px;height:36px}
.faq h2{position:absolute;left:50px;top:11px;font-size:14px;font-weight:400}
.faq-item{position:absolute;left:14px;width:164px}
.faq-item .num{position:absolute;left:0;top:0;width:25px;height:25px;border-radius:50%;background:var(--blue-dark);font-size:10px;text-align:center;line-height:25px}
.faq-item h4{position:absolute;left:45px;top:0;font-size:11px;font-weight:600;white-space:nowrap}
.faq-item p{position:absolute;left:46px;top:20px;width:126px;font-size:9.6px;line-height:13.1px}
.faq .rule{position:absolute;left:14px;width:164px;height:1px;background:rgba(255,255,255,.55)}
.faq .view{position:absolute;left:101px;top:458px;width:76px;height:25px;background:var(--blue-dark);font-size:10.5px;text-align:center;line-height:25px}

.footer{left:0;top:1100px;width:1019px;height:100px;background:var(--footer);color:#e5e5e5;font-size:10.5px;text-align:center}
.footer nav{margin-top:30px;display:flex;justify-content:center}
.footer nav a{color:#e5e5e5;text-decoration:none;padding:0 14px;border-left:1px solid #a0a0a0;line-height:12px;white-space:nowrap}
.footer nav a:first-child{border-left:none}
.footer .copy{margin-top:11px}
</style>
</head>
<body>

<div class="abs topbar">
  <div class="contact" style="left:646px">
    <svg viewBox="0 0 12 12"><rect width="12" height="12" rx="2" fill="var(--blue)"/><path d="M3.5 2.5l1.5 1.5-.8 1.2c.6 1.2 1.4 2 2.6 2.6l1.2-.8 1.5 1.5-1 1.2C5.6 9.5 2.5 6.4 2.3 3.5z" fill="#fff"/></svg>
    +1 555-0142-300
  </div>
  <div class="contact" style="left:757px">
    <svg viewBox="0 0 14 12"><rect y="1" width="14" height="10" rx="1.5" fill="var(--blue)"/><path d="M1 2l6 5 6-5" stroke="#fff" stroke-width="1.2" fill="none"/></svg>
    help@harborhomehealth.example
  </div>
</div>

<header class="abs header">
  <div class="brand"><span class="dot"></span><span class="name">Harbor Home Health</span></div>
  <nav class="nav">
    <a href="#">Home</a><a href="#">About Us</a><a href="#">Services</a><a href="#">Resources</a><a href="#">FAQ</a><a href="#">Employment &amp; Contact</a>
  </nav>
</header>

<section class="abs hero" role="img" aria-label="Black and white close-up of a younger hand holding an elderly person's hands">
  <svg class="arrow" style="left:57px" viewBox="0 0 46 98"><path d="M45 1L1 49l44 48" stroke="#fff" stroke-width="1.3" fill="none"/></svg>
  <svg class="arrow" style="left:918px" viewBox="0 0 46 98"><path d="M1 1l44 48L1 97" stroke="#fff" stroke-width="1.3" fill="none"/></svg>
  <div class="tagline">WE ARE CAREING <b>OLD-AGED PEOPLE</b></div>
  <div class="hours">24<small>Hr</small></div>
  <div class="ring"><div role="img" aria-label="Carer in a blue uniform serving a meal tray to a smiling elderly woman"></div></div>
</section>

<h2 class="abs section-title" style="left:137px;top:570px"><b>OUR</b> SERVICES</h2>

<article class="abs card" style="left:137px">
  <div class="photo" role="img" aria-label="Carer helping an elderly woman exercise" style="background:linear-gradient(120deg,#3a2a2a,#c9b8a8 45%,#2f6fb6 80%,#eee)"></div>
  <svg class="badge" viewBox="0 0 26 30"><path d="M0 0h26v30l-13-7-13 7z" fill="var(--blue)"/><circle cx="13" cy="12" r="6" fill="#fff"/></svg>
  <h3>24hr NURSING CARE</h3>
  <p>Brookfield is a won-derfully warm and friendly home located</p>
  <div class="more">Read More ›</div>
</article>
<article class="abs card" style="left:275px">
  <div class="photo" role="img" aria-label="Doctor checking on an elderly patient" style="background:linear-gradient(120deg,#efe9e0,#d8d2c6 40%,#a89a80 75%,#e6dccb)"></div>
  <svg class="badge" viewBox="0 0 26 30"><path d="M0 0h26v30l-13-7-13 7z" fill="var(--blue)"/><circle cx="14" cy="7" r="2" fill="#fff"/><path d="M8 18l3-5 3 2 2 4M11 13l2-3 4 2" stroke="#fff" stroke-width="1.8" fill="none"/></svg>
  <h3>HOME CARE</h3>
  <p>There are a number of different care cen-tres offering a variety</p>
  <div class="more">Read More ›</div>
</article>
<article class="abs card" style="left:413px">
  <div class="photo" role="img" aria-label="Young plant held in open hands against a cloudy sky" style="background:linear-gradient(180deg,#b7c3cc,#e5e8e6 50%,#7e9a5c 80%,#c9b59a)"></div>
  <svg class="badge" viewBox="0 0 26 30"><path d="M0 0h26v30l-13-7-13 7z" fill="var(--blue)"/><rect x="6" y="7" width="14" height="11" rx="1.5" fill="#fff"/><path d="M13 9v7M9.5 12.5h7" stroke="var(--blue)" stroke-width="2"/></svg>
  <h3>ADVICE CENTRE</h3>
  <p>Many people are forced to make a decision about a care</p>
  <div class="more">Read More ›</div>
</article>
<article class="abs card" style="left:551px">
  <div class="photo" role="img" aria-label="Doctor in a white coat holding a stethoscope" style="background:linear-gradient(110deg,#f3f3f3,#dcdcdc 40%,#8a6a5a 65%,#eeeeee)"></div>
  <svg class="badge" viewBox="0 0 26 30"><path d="M0 0h26v30l-13-7-13 7z" fill="var(--blue)"/><path d="M13 19l-6-6a3.3 3.3 0 0 1 6-4 3.3 3.3 0 0 1 6 4z" fill="#fff"/></svg>
  <h3>ABOUT US</h3>
  <p>Maple Healthcare Ltd is based in the South East of England.</p>
  <div class="more">Read More ›</div>
</article>

<div class="abs about-photo" role="img" aria-label="Close-up of two hands clasped together, young and elderly"></div>
<h2 class="abs section-title" style="left:416px;top:846px"><b>ABOUT</b> US</h2>
<p class="abs about-text" style="left:416px;top:866px;width:258px">There are many variations of passages of Lorem Ipsum available, but the majority have suffered alteration in some form, by injected humour, or randomised words which don't look even slightly believable. If you are going to use a passage of Lorem Ipsum, you need to be sure there isn't anything embarrassing hidden in the middle of text. All the Lorem Ipsum generators on the anything em-</p>
<p class="abs about-text" style="left:137px;top:974px;width:540px;text-align:left">There are many variations of passages of Lorem Ipsum available, but the majority have suffered alteration in some form, Lorem Ipsum, you need to be sure there isn't anything embarrassing.</p>
<div class="abs btn" style="left:601px;top:1015px;width:75px;height:25px">Read More</div>

<aside class="abs faq">
  <svg class="flag" viewBox="0 0 26 36"><path d="M0 0h26v36l-13-6-13 6z" fill="#fff"/><text x="13" y="21" font-family="Roboto,sans-serif" font-weight="700" font-size="15" fill="var(--blue)" text-anchor="middle">?</text></svg>
  <h2>FAQs</h2>
  <div class="faq-item" style="top:55px;height:90px"><span class="num">1</span><h4>Lorem Ipsum is simply</h4><p>Lorem Ipsum has been the industry's standard look dummy text ever since Lorem Ipsum has been the industry's standard</p></div>
  <div class="rule" style="top:156px"></div>
  <div class="faq-item" style="top:171px;height:90px"><span class="num">2</span><h4>Lorem Ipsum is simply</h4><p>Lorem Ipsum has been the industry's standard look dummy text ever since Lorem Ipsum has been the industry's standard</p></div>
  <div class="rule" style="top:274px"></div>
  <div class="faq-item" style="top:295px;height:140px"><span class="num">3</span><h4>Lorem Ipsum is simply</h4><p>Lorem Ipsum has been the industry's standard look dummy text ever since Lorem Ipsum has been the industry's standard dummy text ever since Lorem Ipsum has been the industry's standard look dummy text ever since</p></div>
  <div class="view">View More</div>
</aside>

<footer class="abs footer">
  <nav><a href="#">Home</a><a href="#">About Us</a><a href="#">Services</a><a href="#">Resources</a><a href="#">FAQ</a><a href="#">Employment &amp; Contact</a></nav>
  <div class="copy">Copyright © 2013 harbor home health Allright Reserved</div>
</footer>

</body>
</html>
```